Basic business card

use my newly created logo - and the phrases (Lower Cost of Test & Accelarated New Product Introduction) - and my new email domain / ID - use at conferences / tradeshows

Industry/Entity Type

semiconductor

Contact Information for Business Card

Lewis K Hardy, Owner, communicate via Logo - Lower Test Spend - Leaner Yield Checks, Faster Launch - Ready Sooner, phone +1 480 555 0162, Ridgeview, Nevada, USA, lewis.hardy@vexalon-tsq.com

Font styles to use
Sans Serif

Requirements
Nice to have
• re-use my logo created via Artisan Hive last August (#5918206)

```html
<!DOCTYPE html>
<html lang="en">
<head>
<meta charset="utf-8">
<title>Vexalon-TSQ Business Card</title>
<link href="https://fonts.googleapis.com/css2?family=EB+Garamond:ital,wght@0,400;0,500;0,700;1,400&display=swap" rel="stylesheet">
<style>
  :root {
    --backdrop: #2f3c5a;
    --card-dark: #48546f;
    --card-light: #ffffff;
    --ink-navy: #34405a;
    --ink-soft: #5a6478;
    --text-light: #f4f6fa;
    --accent-orange: #f39a2b;
    --accent-blue: #2a8fd6;
    --accent-green: #6cc04a;
    --accent-sky: #39b7e8;
  }
  * { margin: 0; padding: 0; box-sizing: border-box; }
  html, body {
    width: 1200px; height: 876px; overflow: hidden;
    background: var(--backdrop);
    font-family: "EB Garamond", Georgia, serif;
  }
  .canvas {
    width: 1200px; height: 876px;
    display: flex; align-items: center; justify-content: center; gap: 40px;
  }
  .card {
    position: relative;
    width: 540px; height: 309px;
    border-radius: 3px;
    box-shadow: 0 14px 30px rgba(0,0,0,.35);
    overflow: hidden;
  }
  .card--back { background: var(--card-light); color: var(--ink-navy); }
  .card--front { background: var(--card-dark); color: var(--text-light); }

  .brand-name { font-weight: 500; letter-spacing: .02em; white-space: nowrap; }
  .brand-mark { display: inline-block; vertical-align: middle; }

  .card--back .brand {
    position: absolute; left: 36px; top: 30px;
    display: flex; align-items: center; gap: 10px;
  }
  .card--back .brand-mark { width: 16px; height: 16px; background: var(--accent-blue); }
  .card--back .brand-name { font-size: 34px; color: var(--ink-navy); }

  .holder { position: absolute; left: 36px; top: 96px; }
  .holder-name {
    font-size: 22px; font-weight: 700; letter-spacing: .06em;
    text-transform: uppercase; color: var(--ink-navy);
  }
  .holder-role { font-size: 15px; color: var(--ink-soft); margin-top: -2px; }

  .contact-list { list-style: none; position: absolute; left: 36px; top: 160px; }
  .contact-list li {
    display: flex; align-items: center; gap: 8px;
    font-size: 14.5px; line-height: 22px; color: var(--ink-navy);
  }
  .contact-list svg { width: 12px; height: 12px; flex: none; }

  .card--front .brand {
    position: absolute; left: 0; right: 0; top: 96px;
    display: flex; align-items: center; justify-content: center; gap: 14px;
  }
  .card--front .brand-mark { width: 20px; height: 20px; background: var(--text-light); }
  .card--front .brand-name { font-size: 52px; color: var(--text-light); }

  .tagline {
    position: absolute; left: 40px; right: 40px; bottom: 40px;
    font-style: italic; font-size: 14.5px; letter-spacing: .01em;
    color: var(--text-light); white-space: nowrap;
  }
</style>
</head>
<body>
<main class="canvas">

  <section class="card card--back" aria-label="Business card, contact side">
    <div class="brand">
      <span class="brand-mark" aria-hidden="true"></span>
      <span class="brand-name">VEXALON-TSQ</span>
    </div>

    <div class="holder">
      <p class="holder-name">Lewis K Hardy</p>
      <p class="holder-role">Owner</p>
    </div>

    <ul class="contact-list">
      <li>
        <svg viewBox="0 0 12 12" aria-hidden="true"><path d="M3 1 L5 3.5 L4 4.8 Q5 7 7.2 8 L8.5 7 L11 9 L9.8 11 Q4 10.5 1 3 Z" fill="var(--accent-orange)"/></svg>
        +1 480 555 0162
      </li>
      <li>
        <svg viewBox="0 0 12 12" aria-hidden="true"><rect x="0.5" y="2" width="11" height="8" fill="var(--accent-sky)"/><path d="M0.5 2 L6 6.5 L11.5 2" fill="none" stroke="#fff" stroke-width="1"/></svg>
        lewis.hardy@vexalon-tsq.com
      </li>
      <li>
        <svg viewBox="0 0 12 12" aria-hidden="true"><circle cx="6" cy="6" r="5.2" fill="var(--accent-green)"/><path d="M0.8 6 H11.2 M6 0.8 Q3 6 6 11.2 M6 0.8 Q9 6 6 11.2" fill="none" stroke="#fff" stroke-width=".8"/></svg>
        www.vexalon-tsq.com
      </li>
      <li>
        <svg viewBox="0 0 12 12" aria-hidden="true"><path d="M6 11.5 Q1.5 6.5 1.5 4.5 A4.5 4.5 0 0 1 10.5 4.5 Q10.5 6.5 6 11.5 Z" fill="var(--accent-blue)"/><circle cx="6" cy="4.5" r="1.7" fill="#fff"/></svg>
        Ridgeview, Nevada, USA
      </li>
    </ul>
  </section>

  <section class="card card--front" aria-label="Business card, brand side">
    <div class="brand">
      <span class="brand-mark" aria-hidden="true"></span>
      <span class="brand-name">VEXALON-TSQ</span>
    </div>
    <p class="tagline">Lower Test Spend - Leaner Yield Checks, Faster Launch - Ready Sooner</p>
  </section>

</main>
</body>
</html>
```